NuvaTrel children complimentary food package design

We need to design a bilingual (Arabic & English) baby complimentary powder food label, that is suitable for children from 1 to 10 years old. The primary purpose of this product is support healthy growth in general with special emphasis when the child is picky eater.
We want a design that is elegant, professional and western Looking. It will be printed onto a 400 grams can. The brand is called NuvaTrel. The brand name is composed of two parts: "Nuva" which means advance and "Trel" which means ensured. The design should reflect this concept.
Be as creative as possible and we want the brands to have an classy, premium, elegant and professional feel, look and layout. Below are some requirements:
• Color theme: The general color is red keeping in mind that this product will be presented in different flavours: Vanilla, Chocolate and others.
• Unique ingredients/characteristics have to be mentioned on the front panel. Creative ideas are welcome and I am attaching illustrations from competitive products. The ingredients/characteristics are:
o DHA/AA
o 30 Vitamins & Minerals
o GMO free
• Although the brand name has a shield character, but we are looking to have a special character/emblem on the label that will be registered as a trademark. Creative ideas are welcome. Product images from other companies are attached as a reference. We are not limited to animal characters.
• The current organization of English and Arabic brand name is horizontal however this can be changes according to the designer discretion (e.g vertical).
Usually the label of infant formula can is divided into three parts: Left panel, Front panel and right Panel. Arabic text will be added later, just put a place holder and we will add it locally. We have no limitation for the number of colors. Usually the label has 4 process colors (CMYK) plus a number of spot colors and it is fine to use gold or silver color if deemed necessary for the label.
Updates
Target Market(s)
Children 1 - 10 years of age
Industry/Entity Type
Nutrition
Font styles to use
Look and feel
Each slider illustrates characteristics of the customer's brand and the style your logo design should communicate.

```html
<!DOCTYPE html>
<html lang="en">
<head>
<meta charset="utf-8">
<title>NuvaTrel – Vanilla Flavour Label</title>
<link rel="stylesheet" href="https://fonts.googleapis.com/css2?family=Montserrat:wght@600;700;800&family=Roboto+Condensed:wght@400;700;900&display=swap">
<style>
:root{
  --label-orange:#ef6a3e;
  --label-red:#e24a3a;
  --label-coral:#f58a4f;
  --panel-white:#ffffff;
  --ink:#111111;
  --brand-magenta:#b8336f;
  --badge-pink:#f6b9a6;
  --badge-text:#b8336f;
  --hand-orange:#f39a2a;
  --foot-mauve:#a25069;
  --tiger-yellow:#f7c62a;
  --text-light:#ffffff;
}
*{margin:0;padding:0;box-sizing:border-box}
html,body{width:1200px;height:367px;overflow:hidden;background:#fff}
.label{position:relative;width:1200px;height:367px;overflow:hidden;font-family:"Montserrat",sans-serif}
.label__backdrop{position:absolute;inset:0;background:
  linear-gradient(125deg,var(--label-coral) 0%,var(--label-orange) 35%,var(--label-red) 70%,var(--label-orange) 100%)}
.cloud{position:absolute;left:350px;top:0;width:390px;height:140px}
.brand-name{position:absolute;left:400px;top:50px;width:270px;text-align:center;
  font-weight:800;font-size:50px;line-height:60px;letter-spacing:-1px;color:var(--brand-magenta)}
.mascot{position:absolute;left:660px;top:106px;width:96px;height:96px;border-radius:50%;background:var(--tiger-yellow)}
.roar{position:absolute;left:776px;top:168px;font-weight:800;font-size:17px;color:var(--text-light);letter-spacing:.5px}
.handprints{position:absolute;left:436px;top:188px;width:114px;height:54px;border-radius:40%;background:var(--hand-orange);opacity:.85}
.footprints{position:absolute;left:716px;top:244px;width:76px;height:90px;border-radius:45%;background:var(--foot-mauve);opacity:.75}
.claims{position:absolute;left:508px;top:262px;display:flex;gap:2px;list-style:none}
.claim{width:42px;height:42px;border-radius:50%;background:var(--badge-pink);color:var(--badge-text);
  display:flex;align-items:center;justify-content:center;text-align:center;font-weight:700;font-size:6.5px;line-height:1.1;padding:3px}
.flavour{position:absolute;left:481px;top:314px;width:200px;text-align:center;color:var(--text-light);font-weight:700;font-size:11.5px;line-height:14px}
.net-weight{position:absolute;left:481px;top:341px;width:200px;text-align:center;color:var(--text-light);font-weight:700;font-size:11.5px;line-height:14px}

.nutrition{position:absolute;left:4px;top:4px;width:178px;height:359px;background:var(--panel-white);border:1px solid var(--ink);
  padding:4px 6px;font-family:"Roboto Condensed",sans-serif;color:var(--ink);font-size:8.5px;line-height:1.3}
.nutrition__title{font-weight:900;font-size:21px;line-height:1;border-bottom:1px solid var(--ink);padding-bottom:2px}
.row{display:flex;justify-content:space-between;border-bottom:1px solid var(--ink)}
.row--thick{border-bottom:5px solid var(--ink)}
.row--mid{border-bottom:3px solid var(--ink)}
.row--indent{padding-left:10px}
.b{font-weight:700}
.nutrition__note{font-size:6.5px;line-height:1.2;margin-top:3px}
.dv-table{width:100%;font-size:6.5px;border-collapse:collapse;margin-top:2px}
.dv-table td{padding:0 1px}

.supplement{position:absolute;left:966px;top:4px;width:230px;height:359px;background:var(--panel-white);border:1px solid var(--ink);overflow:hidden}
.supplement__body{position:absolute;left:230px;top:0;width:359px;height:230px;transform-origin:0 0;transform:rotate(90deg);
  padding:4px 6px;font-family:"Roboto Condensed",sans-serif;color:var(--ink);font-size:7px;line-height:1.25}
.supplement__title{font-weight:900;font-size:16px;border-bottom:3px solid var(--ink)}
.supp-table{width:100%;border-collapse:collapse}
.supp-table td{border-bottom:1px solid var(--ink);padding:0 2px}
.supp-table td:last-child,.supp-table td:nth-child(2){text-align:right}
.supplement__note{font-size:6px;margin-top:3px}
</style>
</head>
<body>
<main class="label">
  <div class="label__backdrop" role="img" aria-label="Faceted orange and red low-poly background pattern"></div>

  <section class="nutrition">
    <h2 class="nutrition__title">Nutrition Facts</h2>
    <div class="row">Serving Size (123g)</div>
    <div class="row row--thick">Amount Per Serving</div>
    <div class="row"><span><span class="b">Calories</span> 110</span><span>Calories from Fat 0</span></div>
    <div class="row row--mid" style="justify-content:flex-end"><span class="b">% Daily Value*</span></div>
    <div class="row"><span><span class="b">Total Fat</span> 0g</span><span class="b">0%</span></div>
    <div class="row row--indent"><span>Saturated Fat 0g</span><span class="b">0%</span></div>
    <div class="row row--indent"><span>Trans Fat 0g</span></div>
    <div class="row"><span><span class="b">Cholesterol</span> 0mg</span><span class="b">0%</span></div>
    <div class="row"><span><span class="b">Sodium</span> 0mg</span><span class="b">0%</span></div>
    <div class="row"><span><span class="b">Potassium</span> 450mg</span><span class="b">13%</span></div>
    <div class="row"><span><span class="b">Total Carbohydrate</span> 30g</span><span class="b">10%</span></div>
    <div class="row row--indent"><span>Dietary Fiber 3g</span><span class="b">12%</span></div>
    <div class="row row--indent"><span>Sugars 19g</span></div>
    <div class="row row--thick"><span><span class="b">Protein</span> 1g</span></div>
    <div class="row"><span>Vitamin A 2%</span><span>•</span><span>Vitamin C 15%</span></div>
    <div class="row"><span>Calcium 0%</span><span>•</span><span>Iron 2%</span></div>
    <p class="nutrition__note">*Percent Daily Values are based on a 2,000 calorie diet. Your daily values may be higher or lower depending on your calorie needs.</p>
    <table class="dv-table">
      <tr><td></td><td>Calories</td><td>2,000</td><td>2,500</td></tr>
      <tr><td>Total Fat</td><td>Less than</td><td>65g</td><td>80g</td></tr>
      <tr><td>&nbsp;Saturated Fat</td><td>Less than</td><td>20g</td><td>25g</td></tr>
      <tr><td>Cholesterol</td><td>Less than</td><td>300mg</td><td>300mg</td></tr>
      <tr><td>Sodium</td><td>Less than</td><td>2,400mg</td><td>2,400mg</td></tr>
      <tr><td>Potassium</td><td></td><td>3,500mg</td><td>3,500mg</td></tr>
      <tr><td>Total Carbohydrate</td><td></td><td>300g</td><td>375g</td></tr>
      <tr><td>&nbsp;Dietary Fiber</td><td></td><td>25g</td><td>30g</td></tr>
    </table>
    <p class="nutrition__note">Calories per gram: Fat 9 • Carbohydrate 4 • Protein 4</p>
  </section>

  <svg class="cloud" viewBox="0 0 420 150" preserveAspectRatio="none" aria-hidden="true">
    <path d="M20 40 C 0 0, 60 -10, 110 10 C 150 -5, 230 -8, 290 8 C 350 -6, 420 10, 405 55 C 425 95, 380 130, 320 118 C 270 145, 200 140, 150 125 C 100 145, 30 130, 35 95 C 5 80, 5 60, 20 40 Z" fill="#ffffff"/>
    <path d="M40 50 C 30 20, 80 15, 120 28 C 170 15, 260 15, 300 25 C 350 18, 395 35, 385 65" fill="none" stroke="#f6d2d8" stroke-width="3"/>
  </svg>
  <h1 class="brand-name">NuvaTrel</h1>

  <div class="mascot" role="img" aria-label="Cartoon tiger cub mascot head"></div>
  <p class="roar">RAWRH!!</p>
  <div class="handprints" role="img" aria-label="Two small orange child handprints"></div>
  <div class="footprints" role="img" aria-label="Two small mauve baby footprints"></div>

  <ul class="claims">
    <li class="claim">DHA/AA</li>
    <li class="claim">+30 vitamins &amp; minerals</li>
    <li class="claim">GMO free</li>
  </ul>
  <p class="flavour">Vanilla Flavour</p>
  <p class="net-weight">Net. Wt. 900g Powder</p>

  <section class="supplement">
    <div class="supplement__body">
      <h2 class="supplement__title">Supplement Facts</h2>
      <p>Serving Size: 1 scoop (30g) • Servings Per Container: 30</p>
      <table class="supp-table">
        <tr><td class="b">Amount Per Serving</td><td class="b">Amount</td><td class="b">% DV</td></tr>
        <tr><td>Calories</td><td>120</td><td></td></tr>
        <tr><td>Protein</td><td>4g</td><td>8%</td></tr>
        <tr><td>Vitamin A</td><td>150mcg</td><td>30%</td></tr>
        <tr><td>Vitamin D</td><td>5mcg</td><td>25%</td></tr>
        <tr><td>Vitamin E</td><td>3mg</td><td>20%</td></tr>
        <tr><td>Vitamin C</td><td>20mg</td><td>35%</td></tr>
        <tr><td>Calcium</td><td>250mg</td><td>25%</td></tr>
        <tr><td>Iron</td><td>3mg</td><td>20%</td></tr>
        <tr><td>Zinc</td><td>2mg</td><td>15%</td></tr>
        <tr><td>DHA</td><td>20mg</td><td>†</td></tr>
        <tr><td>AA</td><td>20mg</td><td>†</td></tr>
      </table>
      <p class="supplement__note">Ingredients: skimmed milk powder, vegetable oils, maltodextrin, sugar, whey, vitamins, minerals, natural vanilla flavour. † Daily Value not established. Store in a cool dry place and use within four weeks of opening.</p>
    </div>
  </section>
</main>
</body>
</html>
```